Coldforge Prime manufacturing Project

We are looking at getting a brand new design for a new company that deals in selling stainless tubing and other stainless still products such as handrails, Spigots, Balustrade Fittings
Glass, Glass fittings and Aluminium Channels

We require a very clean website that deals with the following colours:

Blue to light blues
Blacks
Greys to light Greys
Whites

We are open for other ideas BUT we *DO NOT* want any pinks, greens or bright colours except for backgrounds colours we have chosen above. (It can be solid, gradient or a subtle pattern)

YOU MUST KEEP THE LOGO AS IS. PLEASE DO NOT ALTER THE LOGO IN *ANY WAY* and the logo MUST be the same colours and fonts.

Logo is attached.

The site must contain these aspects:
jQuery Slider (Image slide show)
Top drop down Menus
Be no more than 900px wide
Text is to be to the w3C standards. (no special fonts)

We will chop up the design into html format. You just need to provide the PSD file.

The clients opposition is:
www.quorvatrim.example

Industry/Entity Type

It Company

Requirements
Nice to have
• Alter the logo in anyway

Files

```html
<!DOCTYPE html>
<html lang="en">
<head>
<meta charset="utf-8">
<title>Coldforge Prime — Home</title>
<link href="https://fonts.googleapis.com/css2?family=Source+Sans+3:wght@200;300;400;600&family=Arimo:wght@400&display=swap" rel="stylesheet">
<style>
:root{
  --page:#e4e4e8;
  --page-light:#ffffff;
  --ink:#1e1e1e;
  --body:#4a4a4a;
  --muted:#8a8a8a;
  --blue:#4b5b92;
  --blue-btn:#6a78ad;
  --blue-btn-dark:#55639a;
  --bar:#3c3c3e;
  --panel:rgba(40,40,44,.88);
  --rule:#cfcfd4;
  --footer:#474749;
  --footer-text:#a9a9ab;
  --white:#ffffff;
}
*{box-sizing:border-box;margin:0;padding:0}
html,body{width:1000px;height:1200px;overflow:hidden}
body{
  position:relative;
  font-family:"Source Sans 3",sans-serif;
  color:var(--ink);
  background:
    radial-gradient(ellipse 260px 200px at 200px 40px,var(--page-light) 0%,rgba(255,255,255,0) 100%),
    var(--page);
}
.abs{position:absolute}

/* header */
.brand{left:128px;top:8px;width:160px;text-align:center}
.brand-mark{width:56px;height:56px;border-radius:50%;background:#2c2c30;margin:0 auto 8px;border:3px solid #c9c9cf}
.brand-name{font-size:17px;font-weight:400;color:var(--ink);line-height:1}
.brand-sub{font-size:8px;letter-spacing:1.4px;color:var(--ink);margin-top:2px}

.search{left:685px;top:23px;width:185px;height:26px;background:var(--white);border:1px solid #d4d4d8;font-size:11px;color:#aaa;padding:6px 6px}
.search svg{position:absolute;right:5px;top:3px}

.nav{left:369px;top:73px;height:29px;display:flex;align-items:center;font-size:14px}
.nav a{color:var(--ink);text-decoration:none;padding:0 26px;border-left:1px solid #b9b9bf;line-height:17px}
.nav a.active{background:var(--blue-btn);color:var(--white);padding:6px 12px;border:none;margin-right:10px}
.nav a.active + a{border-left:1px solid #b9b9bf}

/* hero */
.hero{left:128px;top:134px;width:743px;height:328px;background:var(--white);box-shadow:0 4px 6px rgba(0,0,0,.12)}
.hero-photo{left:5px;top:6px;width:733px;height:318px;background:linear-gradient(120deg,#8c97a8 0%,#c7cfdc 40%,#9ba7b8 70%,#dde3ee 100%)}
.hero-panel{left:488px;top:193px;width:347px;height:212px;background:var(--panel);padding:14px 16px 0 10px;color:var(--white)}
.hero-title{font-size:37px;font-weight:300;line-height:1.05;white-space:nowrap}
.hero-text{font-size:11.2px;line-height:16.5px;margin:12px 0 0 6px;color:#f0f0f0}
.btn{display:inline-block;background:var(--blue-btn);color:var(--white);text-decoration:none}
.hero .btn,.hero-panel .btn{font-size:13px;padding:6px 10px;margin:15px 0 0 6px;width:105px}

/* sections */
.section-title{font-size:22px;font-weight:600;color:var(--blue);letter-spacing:.2px}
.rule{height:1px;background:var(--rule)}

.card{width:232px}
.card-bar{height:25px;background:var(--bar);color:var(--white);font-size:11.5px;line-height:25px;padding-left:9px}
.card-bar::before{content:"";display:inline-block;width:5px;height:5px;border-radius:50%;background:#aab3d6;margin-right:5px;vertical-align:middle;position:relative;top:-1px}
.card-photo{height:104px;margin-top:3px;border:1px solid #f2f2f2}

.who-sub{font-size:11.5px;font-weight:600;color:var(--ink)}
.who-text{font-family:"Arimo",sans-serif;font-size:10.3px;line-height:15px;color:var(--body)}
.btn-small{font-family:"Source Sans 3",sans-serif;font-size:9.5px;padding:4px 6px}

.catalogue{left:657px;top:863px;width:212px;height:37px;background:linear-gradient(#6b79ae,#4f5d93);color:var(--white);padding:4px 10px}
.catalogue-title{font-size:15px;font-weight:600;letter-spacing:.8px;line-height:1.1}
.catalogue-sub{font-family:"Arimo",sans-serif;font-size:8.5px}
.catalogue svg{position:absolute;right:8px;top:6px}
.catalogue-photo{left:657px;top:906px;width:212px;height:159px;background:var(--white);border:1px solid #d2d2d6;padding:10px}
.catalogue-photo div{width:100%;height:100%;background:radial-gradient(circle at 50% 50%,#cfd2d8 0%,#f6f6f7 70%)}

/* footer */
.footer{left:0;top:1114px;width:1000px;height:86px;background:var(--footer)}
.footer-brand{left:130px;top:8px;width:140px;text-align:center;color:var(--white)}
.footer-brand .brand-mark{width:38px;height:38px;margin-bottom:5px;border-width:2px}
.footer-brand .brand-name{color:var(--white);font-size:14px}
.footer-brand .brand-sub{color:var(--white);font-size:6.5px}
.talk{left:346px;top:12px;color:var(--footer-text);display:flex;align-items:center;gap:8px}
.talk-label{font-size:14px;font-weight:300}
.talk-phone{font-size:30px;font-weight:200;letter-spacing:-.5px}
.footer-rule{left:346px;top:48px;width:347px;height:1px;background:#5c5c5e}
.legal{left:346px;top:61px;font-family:"Arimo",sans-serif;font-size:8.3px;color:var(--footer-text)}
.social{left:722px;top:16px;display:flex;gap:3px}
.social span{width:24px;height:24px;border-radius:50%;background:#8d8d90}
</style>
</head>
<body>

<header>
  <div class="abs brand">
    <div class="brand-mark"></div>
    <div class="brand-name">Coldforge Prime</div>
    <div class="brand-sub">Manufacturing Co. Ltd</div>
  </div>

  <div class="abs search">Search
    <svg width="20" height="20" viewBox="0 0 20 20"><circle cx="8" cy="8" r="5.5" fill="none" stroke="#777" stroke-width="2"/><line x1="12" y1="12" x2="18" y2="18" stroke="#555" stroke-width="3" stroke-linecap="round"/></svg>
  </div>

  <nav class="abs nav">
    <a class="active" href="#">Home</a>
    <a href="#">About Prime</a>
    <a href="#">Products</a>
    <a href="#">Download</a>
    <a href="#" style="padding-right:0">Contact Us</a>
  </nav>
</header>

<section class="abs hero">
  <div class="abs hero-photo" role="img" aria-label="Stainless steel and glass staircase railing"></div>
</section>
<div class="abs hero-panel">
  <h1 class="hero-title">Coldforge Prime</h1>
  <p class="hero-text">simply dummy text of the printing and typesetting industry. Lorem Ipsum has been the industry's standard dummy text ever since the 1500s, when an unknown printer took a galley of type and scrambled it to make a type specimen book. It has survived not only five centuries.</p>
  <a class="btn" href="#">More Details...</a>
</div>

<h2 class="abs section-title" style="left:128px;top:488px">PRIME PRODUCTS</h2>
<div class="abs rule" style="left:128px;top:522px;width:738px"></div>

<div class="abs card" style="left:129px;top:539px"><div class="card-bar">Railing System (42.4,33.7,48.3)</div><div class="card-photo" role="img" aria-label="Handrail bracket on stainless post" style="background:linear-gradient(90deg,#b8bcbf,#9ea4a6)"></div></div>
<div class="abs card" style="left:384px;top:539px"><div class="card-bar">Railing System (42.4,33.7,48.3)</div><div class="card-photo" role="img" aria-label="Polished stainless post base" style="background:linear-gradient(90deg,#c4bcb8,#e2dcd8 50%,#bdb3ae)"></div></div>
<div class="abs card" style="left:641px;top:539px"><div class="card-bar">Glass System (42.4,33.7,48.3)</div><div class="card-photo" role="img" aria-label="Glass clamp on stainless post" style="background:linear-gradient(90deg,#8d90b4,#7f82ad)"></div></div>

<div class="abs card" style="left:129px;top:694px"><div class="card-bar">Post &amp; Balustrade</div><div class="card-photo" role="img" aria-label="Wire balustrade with turnbuckles" style="background:linear-gradient(90deg,#f4f4f4,#e6e6e6)"></div></div>
<div class="abs card" style="left:384px;top:694px"><div class="card-bar">Accessories (42.4,33.7,48.3)</div><div class="card-photo" role="img" aria-label="Wire crimping tool" style="background:linear-gradient(#fafafa,#e4e6ea)"></div></div>
<div class="abs card" style="left:641px;top:694px"><div class="card-bar">Square tube Fittings</div><div class="card-photo" role="img" aria-label="Square tube fitting on timber post" style="background:linear-gradient(90deg,#8fb0b4,#a6c2c4 60%,#8fb0b4)"></div></div>

<h2 class="abs section-title" style="left:128px;top:858px">WHO WE ARE?</h2>
<div class="abs rule" style="left:128px;top:894px;width:503px"></div>
<div class="abs" style="left:129px;top:902px;width:510px">
  <p class="who-sub">Simply dummy text of the printing and typesetting industry.</p>
  <p class="who-text" style="margin-top:5px">simply dummy text of the printing and typesetting industry. Lorem Ipsum has been the industry's standard dummy text ever since the 1500s, when an unknown printer took a galley of type and scrambled it to make a type specimen book. It has survived not only five centuries, but also the leap into electronic typesetting, remaining essentially unchanged.</p>
  <p class="who-text" style="margin-top:15px">simply dummy text of the printing and typesetting industry. Lorem Ipsum has been the industry's standard dummy text ever since the 1500s.</p>
  <a class="btn btn-small" href="#" style="margin-top:17px">More Details...</a>
</div>

<aside>
  <div class="abs catalogue">
    <div class="catalogue-title">Download Catalogue</div>
    <div class="catalogue-sub">New Products</div>
    <svg width="24" height="26" viewBox="0 0 24 26"><path d="M9 2h6v9h5l-8 8-8-8h5z" fill="#222"/><path d="M2 18v5h20v-5" fill="none" stroke="#222" stroke-width="3"/></svg>
  </div>
  <div class="abs catalogue-photo"><div role="img" aria-label="Two polished stainless glass spigots"></div></div>
</aside>

<footer class="abs footer">
  <div class="abs footer-brand">
    <div class="brand-mark"></div>
    <div class="brand-name">Coldforge Prime</div>
    <div class="brand-sub">Manufacturing Co. Ltd</div>
  </div>
  <div class="abs talk">
    <span class="talk-label">Talk to us!</span>
    <svg width="12" height="20" viewBox="0 0 12 20"><path d="M9 1C4 2 2 6 2 10s2 8 7 9l2-4-3-1c-1-2-1-6 0-8l3-1z" fill="#a9a9ab"/></svg>
    <span class="talk-phone">800 555 014</span>
  </div>
  <div class="abs footer-rule"></div>
  <p class="abs legal">©2013 Coldforge Prime. All rights reserved. &nbsp; Privacy Policy &nbsp;| &nbsp;Terms &amp; Conditions</p>
  <div class="abs social"><span></span><span></span><span></span><span></span><span></span></div>
</footer>

</body>
</html>
```